Rack Flyer for Willowcrest Dementia

We need a rack flyer design providing information on services we offer, fees and relevant contact information. Using company branding (logo, font and colours). Must be provided in a format that is easily edited for ongoing use.

For DL size (99 x 210mm)

```html
<!DOCTYPE html>
<html lang="en">
<head>
<meta charset="utf-8">
<title>Willowcrest Dementia – DL Rack Flyer</title>
<link rel="stylesheet" href="https://fonts.googleapis.com/css2?family=Montserrat:ital,wght@0,300;0,400;0,600;0,700;0,800;1,700;1,800&family=Allura&family=Oswald:wght@600&display=swap">
<style>
  :root{
    --navy:#1d1b66;
    --navy-soft:#23237a;
    --navy-deep:#1a1860;
    --gold:#f0a42a;
    --white:#ffffff;
    --frame:#7d7cb8;
    --backdrop:#ececec;
  }
  *{box-sizing:border-box;margin:0;padding:0}
  html,body{width:1200px;height:909px;overflow:hidden;background:var(--backdrop);font-family:'Montserrat',sans-serif}
  .canvas{position:relative;width:1200px;height:909px}
  .flyer{position:absolute;top:72px;width:356px;height:755px;overflow:hidden;background:var(--navy)}
  .flyer--front{left:182px}
  .flyer--back{left:662px}

  /* brand lockup */
  .brand{display:flex;align-items:center;gap:10px;color:var(--navy)}
  .brand__dot{border-radius:50%;border:3px solid var(--navy);flex:none}
  .brand__name{font-family:'Oswald',sans-serif;font-weight:600;line-height:1;letter-spacing:.5px}

  /* front */
  .front__header{position:absolute;inset:0 0 auto 0;height:100px;background:var(--white);display:flex;align-items:center;justify-content:center}
  .front__header .brand__dot{width:46px;height:46px}
  .front__header .brand__name{font-size:26px}
  .front__photo{position:absolute;top:100px;left:0;width:356px;height:399px;
    background:linear-gradient(160deg,#c7a27a 0%,#e2d3bf 35%,#9d8fc2 60%,#6b5a48 100%)}
  .front__intro{position:absolute;top:527px;left:24px;right:20px;color:var(--white);font-size:9.6px;font-weight:300;line-height:12px;text-align:justify}
  .front__intro p+p{margin-top:10px}
  .front__intro p.tight{margin-top:0}
  .front__rule{position:absolute;top:713px;left:0;width:100%;height:4px;background:var(--white)}
  .front__band{position:absolute;top:721px;left:0;width:100%;height:34px;background:var(--gold)}

  /* back */
  .back__title-band{position:absolute;top:0;left:0;width:100%;height:85px;background:var(--navy)}
  .script-title{position:absolute;left:0;right:0;display:flex;justify-content:center;align-items:flex-end;color:var(--gold);font-family:'Allura',cursive;font-weight:400;font-size:40px;line-height:1}
  .script-title::before,.script-title::after{content:"";width:26px;height:1px;background:var(--white);margin-bottom:6px}
  .script-title--services{top:34px}
  .services{position:absolute;top:85px;left:0;width:100%;height:240px;background:var(--navy-soft);list-style:none;padding:20px 28px 0 50px}
  .services li{position:relative;color:var(--white);font-size:9.6px;line-height:11.5px;padding-left:10px;margin-bottom:6.5px}
  .services li::before{content:"";position:absolute;left:0;top:3.5px;width:4px;height:4px;border-right:1.6px solid var(--gold);border-bottom:1.6px solid var(--gold);transform:rotate(-45deg)}
  .back__lower{position:absolute;top:325px;left:0;width:100%;height:331px;background:var(--navy-deep)}

  .fees{position:absolute;top:337px;left:27px;width:302px;height:202px;border:1px solid var(--frame)}
  .script-title--fees{top:8px;font-size:36px}
  .fee{position:absolute;width:0;height:0;color:var(--white)}
  .fee__label{position:absolute;bottom:17px;left:-48px;width:96px;text-align:center;font-size:6.6px;line-height:1.22}
  .fee__ring{position:absolute;left:-33px;top:-33px;width:66px;height:66px}
  .fee__price{position:absolute;left:-40px;top:-11px;width:80px;text-align:center;font-weight:800;font-size:18px;line-height:22px}
  .fee__note{position:absolute;left:-20px;top:10px;width:40px;text-align:center;font-size:4px;font-weight:700}

  .coverage{position:absolute;top:557px;left:25px;right:19px;color:var(--white);font-size:9px;font-weight:300;line-height:11.4px}
  .reach{position:absolute;top:632px;left:25px;color:var(--white);font-size:9.3px;font-weight:800;font-style:italic}
  .back__footer{position:absolute;top:656px;left:0;width:100%;height:68px;background:var(--white)}
  .back__footer .brand{position:absolute;left:32px;top:20px;gap:6px}
  .back__footer .brand__dot{width:24px;height:24px;border-width:2px}
  .back__footer .brand__name{font-size:13px}
  .contact{position:absolute;right:32px;top:11px;text-align:right;color:var(--navy)}
  .contact__phone{font-size:20px;font-weight:700;letter-spacing:.3px}
  .contact__line{font-size:8.5px;line-height:1.3}
  .back__band{position:absolute;top:724px;left:0;width:100%;height:31px;background:var(--gold);display:flex;align-items:center;justify-content:center;color:var(--navy);font-size:7.5px;font-weight:700;font-style:italic}
</style>
</head>
<body>
<div class="canvas">

  <section class="flyer flyer--front">
    <header class="front__header">
      <div class="brand"><span class="brand__dot"></span><span class="brand__name">Willowcrest Dementia</span></div>
    </header>
    <div class="front__photo" role="img" aria-label="Photo of a caregiver comforting an older woman at a kitchen table"></div>
    <div class="front__intro">
      <p>Navigating a diagnosis of dementia can be daunting. You likely have many questions, and it can be overwhelming trying to figure out where to turn to for answers and help. We want you to know that you are not alone in this journey.</p>
      <p>As the numbers of those living with dementia in Bermuda continue to rise placing greater demands on an already strained health care ystem, Willowcrest's clinical and evidence based consultation services improve the safety, independence and quality of life of persons with dementia and their caregivers.</p>
      <p class="tight">Our goal is to assist clients to successfully age in place at home with the support of their family caregivers to reduce the overall cost and burden ofcare for this vulnerable population.</p>
    </div>
    <div class="front__rule"></div>
    <div class="front__band"></div>
  </section>

  <section class="flyer flyer--back">
    <div class="back__title-band"></div>
    <h2 class="script-title script-title--services">Services Offered</h2>
    <ul class="services">
      <li>Comprehensive Dementia Assessment</li>
      <li>Cognitive/Perceptual Screening</li>
      <li>Home Safety Audit (Home modifications and adaptive equipment aids)</li>
      <li>Caregiver Education &amp; Support</li>
      <li>Falls Prevention Strategies</li>
      <li>Personalised Care Planning</li>
      <li>Preparation for future disease progression</li>
      <li>Case Management Support</li>
      <li>Check-in/monitoring visits for clients with limited social support</li>
      <li>Cognitive Stimulation Therapy (group program for individuals with mild-moderate stage dementia)</li>
    </ul>

    <div class="back__lower"></div>
    <div class="fees">
      <h2 class="script-title script-title--fees">Service Fees</h2>

      <div class="fee" style="left:42px;top:96px">
        <div class="fee__label">Initial Consultation</div>
        <svg class="fee__ring" viewBox="0 0 66 66"><circle cx="33" cy="33" r="30" fill="none" stroke="var(--gold)" stroke-width="2.5" stroke-dasharray="125.7 62.8" transform="rotate(-30 33 33)"/></svg>
        <div class="fee__price">$180</div>
      </div>
      <div class="fee" style="left:143px;top:96px">
        <div class="fee__label">Comprehensive Dementia Assessment</div>
        <svg class="fee__ring" viewBox="0 0 66 66"><circle cx="33" cy="33" r="30" fill="none" stroke="var(--gold)" stroke-width="2.5" stroke-dasharray="125.7 62.8" transform="rotate(-30 33 33)"/></svg>
        <div class="fee__price">$395</div>
      </div>
      <div class="fee" style="left:248px;top:96px">
        <div class="fee__label">Comprehensive Dementia Assessment &amp; ongoing case management services</div>
        <svg class="fee__ring" viewBox="0 0 66 66"><circle cx="33" cy="33" r="30" fill="none" stroke="var(--gold)" stroke-width="2.5" stroke-dasharray="125.7 62.8" transform="rotate(-30 33 33)"/></svg>
        <div class="fee__price">$720</div>
      </div>
      <div class="fee" style="left:97px;top:159px">
        <div class="fee__label">Monthly check in<br>monitoring visits</div>
        <svg class="fee__ring" viewBox="0 0 66 66"><circle cx="33" cy="33" r="30" fill="none" stroke="var(--gold)" stroke-width="2.5" stroke-dasharray="125.7 62.8" transform="rotate(-30 33 33)"/></svg>
        <div class="fee__price">$180</div>
      </div>
      <div class="fee" style="left:195px;top:159px">
        <div class="fee__label">Cognitive Stimulation<br>Therapy</div>
        <svg class="fee__ring" viewBox="0 0 66 66"><circle cx="33" cy="33" r="30" fill="none" stroke="var(--gold)" stroke-width="2.5" stroke-dasharray="125.7 62.8" transform="rotate(-30 33 33)"/></svg>
        <div class="fee__price">$500</div>
        <div class="fee__note">per term</div>
      </div>
    </div>

    <p class="coverage">We are pleased to share that services offered by Willowcrest Dementia are currently covered under Harbourline and Coralview health insurance plans. We also have availability of funding support for those in financial need who are unable to afford co-pay, enabling equitable access to these essential care and support services regardless of financial means.</p>
    <p class="reach">Please feel free to reach out for further information.</p>

    <footer class="back__footer">
      <div class="brand"><span class="brand__dot"></span><span class="brand__name">Willowcrest<br>Dementia</span></div>
      <div class="contact">
        <div class="contact__phone">(441) 555 0142</div>
        <div class="contact__line">www.willowcrestdementia.bm</div>
        <div class="contact__line">info@willowcrestdementia.bm</div>
      </div>
    </footer>
    <div class="back__band">Navigating Dementia Together</div>
  </section>

</div>
</body>
</html>
```